A Pharmacy half page colour Ad to be placed in an Asian Newspaper, Promoting our Delivery Service...

We have our company logo available. The main focus of the ad is to promote our free medication delivery service in Edmonton and its surrounding Areas (St. Albert and Sherwood Park) Other points are to talk about our multiculturaly pharmacist who can provide services in Chinese, Vietnamese and English. Another service is our medication organization and packaging services. We also Specialize in providing specialty medications which address liver conditions, and Injectables for Joints, offering the best prices in the city. Free Travel consultations and Administration of travel vaccines is another services.. I guess our overal focus will be on the delivery with these other points included. The ad is a half page. It should communicated a quick and easy delivery services.. with the pharmacy comming to you. Please try to incorporate our colors into the ad.

Target Market(s)

Asian Senior Market

Industry/Entity Type

Pharmacy

Colors

Designer to choose colors to be used in the design.

Requirements
Must have
• Images expressing indicating free delivery.. The best one i saw was an image of white van and it was our Bluefern Pharmacy logo also images which will tell the reader that we are a pharmacy. Clients may not know what pharmacy means.. so we need some kind of image to help communicate this.
• List of our other services..

```html
<!DOCTYPE html>
<html lang="en">
<head>
<meta charset="utf-8">
<title>Bluefern Pharmacy – Free Medication Delivery Service</title>
<link href="https://fonts.googleapis.com/css2?family=Kaushan+Script&family=Poppins:ital,wght@0,600;1,300&family=Saira+Condensed:ital,wght@1,500&display=swap" rel="stylesheet">
<style>
  :root {
    --teal-dark: #1a9aab;
    --teal: #21b0b9;
    --orange: #f5822b;
    --ink: #3c3c3c;
    --white: #ffffff;
    --photo-light: #f4efe9;
    --photo-mid: #c9cdd8;
    --photo-blue: #9fb4e0;
  }
  * { margin: 0; padding: 0; box-sizing: border-box; }
  html, body { width: 1200px; height: 734px; overflow: hidden; background: var(--white); }
  .ad { position: relative; width: 1200px; height: 734px; background: var(--white); }

  .brand-bar {
    position: absolute; left: 0; top: 19px; width: 271px; height: 88px;
    background: var(--teal-dark);
    display: flex; align-items: center; gap: 10px; padding-left: 40px;
  }
  .brand-dot { width: 22px; height: 22px; border-radius: 50%; background: var(--white); flex: none; }
  .brand-name {
    font-family: 'Poppins', sans-serif; font-weight: 600; font-size: 21px;
    line-height: 1.05; color: var(--white);
  }

  .hero-photo {
    position: absolute; left: 0; top: 107px; width: 661px; height: 518px;
    background: linear-gradient(110deg, var(--photo-light) 0%, var(--photo-blue) 35%, var(--photo-mid) 60%, var(--photo-light) 100%);
  }

  .headline {
    position: absolute; left: 700px; top: 20px; width: 460px;
    font-family: 'Kaushan Script', cursive; color: var(--teal);
    text-align: center; line-height: 0.95;
  }
  .headline .free { display: block; font-size: 118px; padding-left: 170px; text-align: left; }
  .headline .medication { display: block; font-size: 104px; letter-spacing: -4px; margin-top: -14px; }

  .tagline {
    position: absolute; left: 755px; top: 274px; width: 345px; height: 44px;
    background: var(--orange); color: var(--white);
    font-family: 'Saira Condensed', sans-serif; font-style: italic; font-weight: 500;
    font-variant: small-caps; font-size: 34px; letter-spacing: 2px;
    display: flex; align-items: center; justify-content: center; line-height: 1;
  }

  .services {
    position: absolute; left: 710px; top: 344px; width: 470px; list-style: none;
    font-family: 'Poppins', sans-serif; font-style: italic; font-weight: 300;
    font-size: 16px; line-height: 22px; color: var(--ink);
  }
  .services li { position: relative; padding-left: 12px; margin-bottom: 22px; }
  .services li::before { content: "*"; position: absolute; left: 0; top: -2px; }

  .contact-band {
    position: absolute; left: 0; top: 662px; width: 1200px; height: 72px;
    background: var(--teal); color: var(--white);
    display: flex; align-items: center; justify-content: center; gap: 30px;
    font-family: 'Poppins', sans-serif; font-style: italic; font-weight: 300; font-size: 28px;
  }
</style>
</head>
<body>
<main class="ad">
  <div class="brand-bar">
    <span class="brand-dot"></span>
    <span class="brand-name">Bluefern<br>Pharmacy</span>
  </div>

  <div class="hero-photo" role="img" aria-label="Photo of a smiling nurse in blue scrubs talking with a senior woman seated in an armchair, holding a glass of water"></div>

  <h1 class="headline">
    <span class="free">Free</span>
    <span class="medication">Medication</span>
  </h1>
  <div class="tagline">Delivery Service</div>

  <ul class="services">
    <li>Delivers to Edmonton and its surrounding Areas<br>&nbsp;(St. Albert and Sherwood Park)</li>
    <li>Services in English, Chinese and Vietnamese language</li>
    <li>Provide medication organization and packaging<br>&nbsp;services</li>
    <li>Provide specialty medications which address liver<br>&nbsp;conditions and Injectables for Joints</li>
    <li>Free Travel consultations and Administration of<br>&nbsp;travel vaccines is another services</li>
  </ul>

  <footer class="contact-band">
    <span class="web">www.bluefernpharmacy.com</span>
    <span class="divider">|</span>
    <span class="phone">045 20418 733 19</span>
  </footer>
</main>
</body>
</html>
```